REAL PSYCHIC rear window decal. Mystical, light, positive, spiritual coach vibes

Design a sign for my back car window.
HOT PINK and purple swirly, mystical sign. Eye-catching and classy.
Size 24” x 18”
TEXT:
MARLENE DOVE
Psychic & Medium
Www,.marlenedove.com
World Renowned for Over 45 Years. (This last line make small at bottom)

*This is not a filled in magnet, it will be transparent.

Target Market(s)

Women

Industry/Entity Type

Spirituality

Font styles to use
Script
Other font styles liked:
• See upload for a font I like

Colors
E54698
E96AAD
F1A4CE
F9D9EA
FCEFF6
A7469A
B969AE
D3A5CF
EDDBEB
F8F0F9
6B429C
8869AF
B7A5CE
E3DAEB
F3F0F8

Requirements
Must have
• Pink purple, classy yet mystical vibe
Nice to have
• Easy to read, but old-timey classic font for “MARLENE DOVE”

```html
<!DOCTYPE html>
<html lang="en">
<head>
<meta charset="utf-8">
<title>Marlene Dove – Psychic &amp; Medium Window Decal</title>
<link rel="stylesheet" href="https://fonts.googleapis.com/css2?family=Lancelot&display=swap">
<style>
  :root {
    --hot-pink: #e8168c;
    --plum: #8e2c8e;
    --blush: #fce9ee;
    --paper: #ffffff;
    --flourish-tone: rgba(142, 44, 142, 0.28);
  }
  html, body {
    margin: 0;
    padding: 0;
    width: 1200px;
    height: 829px;
    overflow: hidden;
    background: var(--paper);
  }
  .decal {
    position: relative;
    width: 1200px;
    height: 829px;
    background: var(--paper);
    font-family: "Lancelot", serif;
    overflow: hidden;
  }
  .decal__backdrop {
    position: absolute;
    inset: 0;
    width: 1200px;
    height: 829px;
  }
  .decal__backdrop .blob { fill: var(--blush); }
  .decal__backdrop .dots { fill: var(--plum); }
  .flourish {
    position: absolute;
    left: 443px;
    width: 318px;
    height: 131px;
    border-radius: 50%;
    background: radial-gradient(ellipse at center, var(--flourish-tone) 0%, rgba(142, 44, 142, 0.08) 65%, rgba(142, 44, 142, 0) 100%);
  }
  .flourish--top { top: 68px; }
  .flourish--bottom { top: 563px; }
  .line {
    position: absolute;
    left: 0;
    width: 1200px;
    margin: 0;
    text-align: center;
    line-height: 1;
    white-space: nowrap;
    font-weight: 400;
  }
  .decal__name {
    top: 228px;
    font-size: 172px;
    color: var(--hot-pink);
  }
  .decal__role {
    top: 389px;
    font-size: 56px;
    color: var(--plum);
  }
  .decal__web {
    top: 468px;
    font-size: 56px;
    color: var(--plum);
  }
  .decal__tagline {
    top: 747px;
    font-size: 32px;
    color: var(--hot-pink);
  }
</style>
</head>
<body>
  <main class="decal">
    <svg class="decal__backdrop" viewBox="0 0 1200 829" aria-hidden="true">
      <path class="blob" d="M0 0 H201 C222 70 200 120 150 150 C95 185 60 240 0 318 Z"/>
      <path class="blob" d="M1200 141 C1180 230 1165 330 1120 375 C1060 430 960 450 905 510 C850 575 880 720 845 829 H1200 Z"/>
      <g id="dot-rule" class="dots">
        <circle cx="185" cy="138" r="2"/>
        <circle cx="204" cy="138" r="2"/>
        <circle cx="223" cy="138" r="2.2"/>
        <circle cx="242" cy="138" r="2.4"/>
        <circle cx="261" cy="138" r="2.6"/>
        <circle cx="280" cy="138" r="2.8"/>
        <circle cx="299" cy="138" r="3"/>
        <circle cx="318" cy="138" r="3.2"/>
        <circle cx="337" cy="138" r="3.5"/>
        <circle cx="356" cy="138" r="3.8"/>
        <circle cx="375" cy="138" r="4.2"/>
        <circle cx="394" cy="138" r="4.6"/>
        <circle cx="412" cy="138" r="5.2"/>
        <circle cx="429" cy="138" r="6"/>
        <circle cx="1013" cy="138" r="2"/>
        <circle cx="994" cy="138" r="2"/>
        <circle cx="975" cy="138" r="2.2"/>
        <circle cx="956" cy="138" r="2.4"/>
        <circle cx="937" cy="138" r="2.6"/>
        <circle cx="918" cy="138" r="2.8"/>
        <circle cx="899" cy="138" r="3"/>
        <circle cx="880" cy="138" r="3.2"/>
        <circle cx="861" cy="138" r="3.5"/>
        <circle cx="842" cy="138" r="3.8"/>
        <circle cx="823" cy="138" r="4.2"/>
        <circle cx="804" cy="138" r="4.6"/>
        <circle cx="786" cy="138" r="5.2"/>
        <circle cx="769" cy="138" r="6"/>
      </g>
      <use href="#dot-rule" y="485"/>
    </svg>

    <div class="flourish flourish--top" role="img" aria-label="Purple swirling scroll flourish ornament"></div>

    <h1 class="line decal__name">Marlene Dove</h1>
    <p class="line decal__role">Psychic &amp; Medium</p>
    <p class="line decal__web">www.marlenedove.com</p>

    <div class="flourish flourish--bottom" role="img" aria-label="Purple swirling scroll flourish ornament"></div>

    <p class="line decal__tagline">World Renowned for Over 45 Years.</p>
  </main>
</body>
</html>
```